Create look and feel for existing Web Page

Update Web Page

We have a website at http://www.getmirvo.com/index-web.html. It is a single page html site, with a custom signup form. We also have a zen desk plugin at the bottom of the page. We'd like to redesign the look and feel of the entire site. We sell software to eye doctors. Also called optometrists, our software tool makes it easy for doctors to manage patients, bill, and document patient encounters. I have included our logos below.

We are looking for a new design preferably in HTML 5, CSS etc. The fields on the form on this page: http://www.getmirvo.com/index-web.html

You can get screen shots of our software application at this site: http://staging.getmirvo.com
username: test@sampledomain-mirvo.com
password: password

```html
<!DOCTYPE html>
<html lang="en">
<head>
<meta charset="utf-8">
<title>Mirvo – Landing Page Variations</title>
<link rel="stylesheet" href="https://fonts.googleapis.com/css2?family=Montserrat:wght@300;400;600;700&display=swap">
<style>
  :root {
    --board: #8c8c8c;
    --white: #ffffff;
    --ink: #222222;
    --muted: #8a8a8a;
    --orange: #f2591a;
    --orange-light: #ff8a1e;
    --blue: #1e9be8;
    --blue-deep: #0a5fd0;
    --footer: #5f5856;
    --black-tab: #1a1a1a;
  }
  html, body { margin: 0; padding: 0; width: 1200px; height: 889px; overflow: hidden; background: var(--board); }
  .board { display: block; width: 1200px; height: 889px; }
  .board text { font-family: 'Montserrat', sans-serif; }
  .logo-name { fill: var(--white); font-size: 26px; font-weight: 400; letter-spacing: 0.5px; }
  .nav-link { fill: var(--white); font-size: 4.6px; font-weight: 600; }
  .btn-label { fill: var(--white); font-size: 3.6px; font-weight: 700; }
  .hero-line { fill: var(--white); font-size: 12px; font-weight: 600; }
  .hero-accent { fill: var(--orange); font-size: 12px; font-weight: 600; }
  .section-title { fill: var(--ink); font-size: 12px; font-weight: 700; }
  .section-sub { fill: var(--orange); font-size: 12px; font-weight: 300; }
  .light-title { fill: var(--white); font-size: 12px; font-weight: 700; }
  .light-sub { fill: var(--white); font-size: 12px; font-weight: 300; }
  .body-white { fill: var(--white); font-size: 3.8px; }
  .body-muted { fill: var(--muted); font-size: 3.5px; }
  .body-dark { fill: #444; font-size: 3.9px; }
  .card-label { fill: var(--ink); font-size: 4.4px; font-weight: 700; }
  .form-title { fill: var(--ink); font-size: 6.4px; font-weight: 700; }
  .form-field { fill: var(--muted); font-size: 3px; }
  .tab-label { fill: var(--white); font-size: 4px; font-weight: 700; }
  .price { fill: var(--orange); font-size: 10px; font-weight: 600; }
  .price-note { fill: #b0b0b0; font-size: 3.2px; }
  .footer-link { fill: var(--white); font-size: 4.4px; }
  .footer-copy { fill: #d8d2cf; font-size: 3px; }
  .partner-name { fill: var(--white); font-size: 7px; font-weight: 400; }
  .page-card { fill: var(--white); }
  .service-card { fill: var(--white); stroke: #eeeeee; stroke-width: 0.6; }
  .icon-stroke { fill: none; stroke: #555; stroke-width: 1.2; stroke-linecap: round; stroke-linejoin: round; }
  .icon-accent { fill: none; stroke: var(--orange); stroke-width: 1.2; stroke-linecap: round; stroke-linejoin: round; }
  .btn-orange { fill: var(--orange); }
  .btn-blue { fill: var(--blue); }
  .rule-orange { stroke: var(--orange); stroke-width: 1; }
  .field-line { stroke: #e2e2e2; stroke-width: 0.5; }
</style>
</head>
<body>
<svg class="board" viewBox="0 0 2231 1652" width="1200" height="889" xmlns="http://www.w3.org/2000/svg">
  <defs>
    <linearGradient id="grad-blue" x1="0" y1="0" x2="1" y2="1">
      <stop offset="0" stop-color="#22a3ee"/>
      <stop offset="1" stop-color="#0a5ad0"/>
    </linearGradient>
    <linearGradient id="grad-orange" x1="0" y1="0" x2="1" y2="1">
      <stop offset="0" stop-color="#ff8c1f"/>
      <stop offset="1" stop-color="#ff5412"/>
    </linearGradient>
    <linearGradient id="grad-device" x1="0" y1="0" x2="1" y2="1">
      <stop offset="0" stop-color="#f4f6f9"/>
      <stop offset="1" stop-color="#c9d3de"/>
    </linearGradient>
    <linearGradient id="hero-1" x1="0" y1="0" x2="1" y2="1"><stop offset="0" stop-color="#a89f96"/><stop offset="1" stop-color="#e4ded7"/></linearGradient>
    <linearGradient id="hero-2" x1="0" y1="0" x2="1" y2="1"><stop offset="0" stop-color="#8c8580"/><stop offset="1" stop-color="#e2dfdb"/></linearGradient>
    <linearGradient id="hero-3" x1="0" y1="0" x2="1" y2="1"><stop offset="0" stop-color="#24405f"/><stop offset="1" stop-color="#8a9fb6"/></linearGradient>
    <linearGradient id="hero-4" x1="0" y1="0" x2="1" y2="1"><stop offset="0" stop-color="#3a3835"/><stop offset="1" stop-color="#8c8173"/></linearGradient>
    <linearGradient id="hero-5" x1="0" y1="0" x2="1" y2="1"><stop offset="0" stop-color="#6a5646"/><stop offset="1" stop-color="#2c3954"/></linearGradient>
    <filter id="page-shadow" x="-5%" y="-2%" width="110%" height="104%">
      <feDropShadow dx="0" dy="2" stdDeviation="3" flood-color="#000" flood-opacity="0.35"/>
    </filter>
    <filter id="card-shadow" x="-10%" y="-10%" width="120%" height="120%">
      <feDropShadow dx="0" dy="1" stdDeviation="1.5" flood-color="#000" flood-opacity="0.15"/>
    </filter>

    <!-- service icons, 24 x 24 -->
    <g id="icon-schedule"><rect class="icon-stroke" x="2" y="4" width="18" height="16" rx="1"/><line class="icon-stroke" x1="2" y1="8" x2="20" y2="8"/><line class="icon-stroke" x1="6" y1="2" x2="6" y2="6"/><line class="icon-stroke" x1="16" y1="2" x2="16" y2="6"/><path class="icon-stroke" d="M5 11h2M9 11h2M13 11h2M5 14h2M9 14h2"/><circle class="icon-accent" cx="18" cy="18" r="4.5"/><path class="icon-accent" d="M18 16v2.3h1.8"/></g>
    <g id="icon-intake"><rect class="icon-stroke" x="3" y="5" width="14" height="17" rx="1"/><path class="icon-stroke" d="M6 10h6M6 13h8M6 16h5"/><circle class="icon-accent" cx="18" cy="6" r="4"/><circle class="icon-accent" cx="18" cy="6" r="1.4"/></g>
    <g id="icon-chart"><path class="icon-stroke" d="M3 22h18"/><rect class="icon-stroke" x="5" y="15" width="3" height="7"/><rect class="icon-stroke" x="10" y="11" width="3" height="11"/><rect class="icon-stroke" x="15" y="7" width="3" height="15"/><path class="icon-accent" d="M4 12l6-5 4 3 7-7M17 3h4v4"/></g>
    <g id="icon-bill"><rect class="icon-stroke" x="3" y="5" width="14" height="17" rx="1"/><path class="icon-stroke" d="M6 10h5M6 13h8M6 16h8M6 19h5"/><circle class="icon-accent" cx="18" cy="6" r="4.5"/><path class="icon-accent" d="M18 3.8v4.4M16.8 5.2h2.2"/></g>
    <g id="icon-eligible"><path class="icon-stroke" d="M20 11a9 9 0 1 1-4-7.5"/><path class="icon-accent" d="M7 11l4 4 10-11"/></g>
    <g id="icon-review"><rect class="icon-stroke" x="3" y="3" width="14" height="18" rx="1"/><path class="icon-stroke" d="M6 7h8M6 10h8M6 13h6M6 16h4"/><path class="icon-accent" d="M18 13l1.3 2.7 2.9.4-2.1 2 .5 2.9-2.6-1.4-2.6 1.4.5-2.9-2.1-2 2.9-.4z"/></g>

    <g id="service-card">
      <rect class="service-card" x="0" y="0" width="96" height="95"/>
    </g>

    <!-- full page body, shared by every hero variation -->
    <g id="page-body">
      <polygon class="page-card" points="0,247 398,195 398,1442 0,1442"/>

      <!-- header -->
      <text class="logo-name" x="46" y="29">mirvo</text>
      <text class="nav-link" x="163" y="22">HOME</text>
      <line class="rule-orange" x1="163" y1="24.5" x2="177" y2="24.5" stroke-width="0.8"/>
      <text class="nav-link" x="191" y="22">PRODUCTS</text>
      <text class="nav-link" x="232" y="22">PRICING</text>
      <text class="nav-link" x="266" y="22">SIGN UP</text>
      <rect class="btn-orange" x="301" y="15" width="47" height="9"/>
      <text class="btn-label" x="324.5" y="20.8" text-anchor="middle">REQUEST A DEMO</text>

      <!-- hero copy -->
      <text class="hero-line" x="48" y="90">LEASE PRACTICES:</text>
      <text class="hero-accent" x="48" y="106">CHOOSE HOW YOU SPEND</text>
      <text class="hero-line" x="48" y="122">YOUR TIME</text>
      <rect class="btn-orange" x="48" y="135" width="120" height="11"/>
      <text class="btn-label" x="108" y="141.8" text-anchor="middle">STOP WASTING MONEY ON PAPER TODAY ›</text>
      <g fill="none" stroke="#ffffff" stroke-width="0.6" opacity="0.8">
        <circle cx="52" cy="186" r="2.2"/><circle cx="84" cy="186" r="2.2"/>
      </g>
      <g fill="#ffffff" opacity="0.8">
        <circle cx="59" cy="186" r="1"/><circle cx="63" cy="186" r="1" fill="#f2591a"/><circle cx="67" cy="186" r="1"/><circle cx="71" cy="186" r="1"/><circle cx="75" cy="186" r="1"/>
      </g>
      <path d="M195 219l4 3 4-3" fill="none" stroke="#999" stroke-width="0.8"/>

      <!-- about band -->
      <polygon points="10,263 388,212 388,417 10,377" fill="url(#grad-blue)"/>
      <rect x="52" y="258" width="136" height="138" rx="4" fill="url(#grad-device)" role="img" aria-label="Desktop monitor showing the Mirvo patient dashboard"/>
      <text x="219" y="258"><tspan class="light-title">ABOUT </tspan><tspan class="light-sub">MIRVO</tspan></text>
      <text class="body-white" x="219" y="281">Sed ut perspiciatis unde omnis iste natus error sit</text>
      <text class="body-white" x="219" y="288">voluptatem accusantium doloremque laudantium,</text>
      <text class="body-white" x="219" y="295">totam rem aperiam, eaque ipsa quae ab.</text>
      <g class="body-white">
        <text x="219" y="311">● Nemo enim ipsam voluptatem quia voluptas</text>
        <text x="219" y="319">● Sed ut perspiciatis unde omnis iste natus error</text>
        <text x="219" y="327">● Lorem ipsum dolor sit amet consectetur</text>
        <text x="223" y="335">adipiscing elit, sed do eiusmod</text>
        <text x="219" y="344">● Sed ut perspiciatis unde omnis iste natus error</text>
      </g>
      <rect class="btn-orange" x="219" y="366" width="50" height="11"/>
      <text class="btn-label" x="244" y="372.6" text-anchor="middle">Learn More</text>

      <!-- services -->
      <text class="section-title" x="199" y="449" text-anchor="middle">AI TO AUTOMATE</text>
      <text class="section-sub" x="199" y="465" text-anchor="middle">OPTOMETRY OFFICE TASKS</text>

      <g transform="translate(47,493)"><use href="#service-card"/><use href="#icon-schedule" transform="translate(36,8)"/><text class="card-label" x="48" y="48" text-anchor="middle">SCHEDULE</text></g>
      <g transform="translate(151,493)"><use href="#service-card"/><use href="#icon-intake" transform="translate(36,8)"/><text class="card-label" x="48" y="48" text-anchor="middle">INTAKE</text></g>
      <g transform="translate(254,493)"><use href="#service-card"/><use href="#icon-chart" transform="translate(36,8)"/><text class="card-label" x="48" y="48" text-anchor="middle">CHART</text></g>
      <g transform="translate(47,603)"><use href="#service-card"/><use href="#icon-bill" transform="translate(36,8)"/><text class="card-label" x="48" y="48" text-anchor="middle">BILL</text></g>
      <g transform="translate(151,603)"><use href="#service-card"/><use href="#icon-eligible" transform="translate(36,8)"/><text class="card-label" x="48" y="48" text-anchor="middle">ELIGIBLE</text></g>
      <g transform="translate(254,603)"><use href="#service-card"/><use href="#icon-review" transform="translate(36,8)"/><text class="card-label" x="48" y="48" text-anchor="middle">REVIEW</text></g>
      <g class="service-copy">
        <g transform="translate(95,0)"><line class="rule-orange" x1="-4" y1="545" x2="4" y2="545"/><g class="body-muted" text-anchor="middle"><text y="557">Sed ut perspiciatis unde omnis</text><text y="562">iste natus error sit volupt atem</text><text y="567">accusa nrium doloremque</text><text y="572">laudan tium totam rem</text></g></g>
        <g transform="translate(199,0)"><line class="rule-orange" x1="-4" y1="545" x2="4" y2="545"/><g class="body-muted" text-anchor="middle"><text y="557">Sed ut perspiciatis unde omnis</text><text y="562">iste natus error sit volupt atem</text><text y="567">accusa nrium doloremque</text><text y="572">laudan tium totam rem</text></g></g>
        <g transform="translate(302,0)"><line class="rule-orange" x1="-4" y1="545" x2="4" y2="545"/><g class="body-muted" text-anchor="middle"><text y="557">Sed ut perspiciatis unde omnis</text><text y="562">iste natus error sit volupt atem</text><text y="567">accusa nrium doloremque</text><text y="572">laudan tium totam rem</text></g></g>
        <g transform="translate(95,110)"><line class="rule-orange" x1="-4" y1="545" x2="4" y2="545"/><g class="body-muted" text-anchor="middle"><text y="557">Sed ut perspiciatis unde omnis</text><text y="562">iste natus error sit volupt atem</text><text y="567">accusa nrium doloremque</text><text y="572">laudan tium totam rem</text></g></g>
        <g transform="translate(199,110)"><line class="rule-orange" x1="-4" y1="545" x2="4" y2="545"/><g class="body-muted" text-anchor="middle"><text y="557">Sed ut perspiciatis unde omnis</text><text y="562">iste natus error sit volupt atem</text><text y="567">accusa nrium doloremque</text><text y="572">laudan tium totam rem</text></g></g>
        <g transform="translate(302,110)"><line class="rule-orange" x1="-4" y1="545" x2="4" y2="545"/><g class="body-muted" text-anchor="middle"><text y="557">Sed ut perspiciatis unde omnis</text><text y="562">iste natus error sit volupt atem</text><text y="567">accusa nrium doloremque</text><text y="572">laudan tium totam rem</text></g></g>
      </g>
      <rect class="btn-orange" x="160" y="720" width="78" height="10"/>
      <text class="btn-label" x="199" y="726.3" text-anchor="middle">VIEW ALL SERVICES ›</text>

      <!-- demo request band -->
      <polygon points="10,765 388,806 388,925 10,972" fill="url(#grad-orange)"/>
      <text class="light-title" x="48" y="826">START USING</text>
      <text class="light-sub" x="48" y="841">MIRVO TODAY</text>
      <line x1="48" y1="851" x2="56" y2="851" stroke="#ffffff" stroke-width="0.8"/>
      <text class="body-white" x="48" y="869">Become part of a club that wants to</text>
      <text class="body-white" x="48" y="877">change the way we practice, so we can</text>
      <text class="body-white" x="48" y="885">have a life outside of the office.</text>
      <rect class="btn-blue" x="48" y="908" width="64" height="10"/>
      <text class="btn-label" x="80" y="914.3" text-anchor="middle">GET STARTED ›</text>

      <g filter="url(#card-shadow)"><rect class="page-card" x="227" y="768" width="120" height="152" rx="2"/></g>
      <text class="form-title" x="237" y="786">REQUEST A DEMO</text>
      <line class="field-line" x1="237" y1="792" x2="337" y2="792"/>
      <text class="form-field" x="237" y="806">Enter Name</text><line class="field-line" x1="237" y1="811" x2="337" y2="811"/>
      <text class="form-field" x="237" y="826">Enter Email</text><line class="field-line" x1="237" y1="831" x2="337" y2="831"/>
      <text class="form-field" x="237" y="846">Cell Phone</text><line class="field-line" x1="237" y1="851" x2="337" y2="851"/>
      <text class="form-field" x="237" y="866">Office Name</text><line class="field-line" x1="237" y1="871" x2="337" y2="871"/>
      <text class="form-field" x="237" y="886">NPI</text><line class="field-line" x1="237" y1="891" x2="337" y2="891"/>
      <rect class="btn-orange" x="237" y="902" width="88" height="9"/>
      <text class="btn-label" x="281" y="907.8" text-anchor="middle">GET THE FREE CHARTING TOOL</text>

      <!-- pricing -->
      <text x="199" y="1002" text-anchor="middle"><tspan class="section-title">PRICING </tspan><tspan class="section-sub">PLAN</tspan></text>
      <line class="rule-orange" x1="193" y1="1011" x2="205" y2="1011"/>
      <text class="body-muted" x="199" y="1030" text-anchor="middle">Lorem ipsum dolor sit amet, consectetur adipiscing elit, sed do eiusmod tempor incididunt ut labore et</text>
      <text class="body-muted" x="199" y="1039" text-anchor="middle">dolore magna aliquis ipsum suspendisse ultrices gravidous commodo.</text>

      <g fill="none" stroke="#777" stroke-width="0.7">
        <circle cx="40" cy="1123" r="5"/><path d="M41.5 1120.5l-2.5 2.5 2.5 2.5"/>
        <circle cx="358" cy="1123" r="5"/><path d="M356.5 1120.5l2.5 2.5-2.5 2.5"/>
      </g>

      <g transform="translate(56,1063)">
        <g filter="url(#card-shadow)"><rect class="page-card" width="92" height="115"/></g>
        <polygon points="2,0 64,0 56,10 2,10" fill="var(--black-tab)"/>
        <text class="tab-label" x="24" y="6.4">FREE</text>
        <text class="body-dark" x="8" y="29">Chart patient findings for FREE.</text>
        <text class="body-dark" x="8" y="38">Unlimited users, doctors,</text>
        <text class="body-dark" x="8" y="47">and location.</text>
        <text class="price" x="8" y="70">$0</text>
        <text class="price-note" x="8" y="82">No strings attached</text>
        <rect class="btn-blue" x="8" y="93" width="46" height="10"/>
        <text class="btn-label" x="31" y="99.3" text-anchor="middle">SIGN UP ›</text>
      </g>
      <g transform="translate(153,1063)">
        <g filter="url(#card-shadow)"><rect class="page-card" width="92" height="115"/></g>
        <polygon points="2,0 64,0 56,10 2,10" fill="var(--black-tab)"/>
        <text class="tab-label" x="8" y="6.4">PICK 1 ADD ON</text>
        <text class="body-dark" x="8" y="29">Choose between schedule,</text>
        <text class="body-dark" x="8" y="38">intake, bill, eligible, or</text>
        <text class="body-dark" x="8" y="47">review.</text>
        <text class="price" x="8" y="70">$99 / mo</text>
        <text class="price-note" x="8" y="82">per location</text>
        <rect class="btn-blue" x="8" y="93" width="46" height="10"/>
        <text class="btn-label" x="31" y="99.3" text-anchor="middle">SIGN UP ›</text>
      </g>
      <g transform="translate(249,1063)">
        <g filter="url(#card-shadow)"><rect class="page-card" width="92" height="115"/></g>
        <polygon points="2,0 64,0 56,10 2,10" fill="var(--black-tab)"/>
        <text class="tab-label" x="8" y="6.4">PICK 2 ADD-ONS</text>
        <text class="body-dark" x="8" y="29">Choose any two features</text>
        <text class="body-dark" x="8" y="38">between schedule, intake, bill,</text>
        <text class="body-dark" x="8" y="47">eligible, and/or review.</text>
        <text class="price" x="8" y="70">$189 / mo</text>
        <text class="price-note" x="8" y="82">per location</text>
        <rect class="btn-blue" x="8" y="93" width="46" height="10"/>
        <text class="btn-label" x="31" y="99.3" text-anchor="middle">SIGN UP ›</text>
      </g>

      <!-- closing call to action -->
      <text class="section-title" x="199" y="1235" text-anchor="middle">NOW SPEND TIME</text>
      <text class="section-sub" x="199" y="1251" text-anchor="middle">OUTSIDE THE OFFICE!</text>
      <text class="body-dark" x="199" y="1283" text-anchor="middle" fill="#666">Lorem ipsum dolor sit amet, consectetur adipiscing elit, sed do eiusmod tempor incididunt</text>
      <text class="body-dark" x="199" y="1292" text-anchor="middle" fill="#666">ut labore et dolore magna aliquis ipsum suspendisse ultrices gravidous commodo.</text>
      <rect class="btn-orange" x="160" y="1310" width="78" height="10"/>
      <text class="btn-label" x="199" y="1316.3" text-anchor="middle">JOIN THE CLUB ›</text>

      <!-- footer -->
      <polygon points="0,1392 398,1342 398,1442 0,1442" fill="var(--footer)"/>
      <path d="M195 1368l4-3 4 3" fill="none" stroke="#ffffff" stroke-width="0.8"/>
      <g fill="none" stroke="#ffffff" stroke-width="0.8">
        <circle cx="68" cy="1409" r="7"/><circle cx="88" cy="1409" r="7"/><circle cx="128" cy="1409" r="7"/>
      </g>
      <circle cx="108" cy="1409" r="7" fill="var(--orange)"/>
      <text class="footer-link" x="157" y="1411">HOME</text>
      <text class="footer-link" x="184" y="1411">PRODUCTS</text>
      <text class="footer-link" x="225" y="1411">PRICING</text>
      <text class="footer-link" x="258" y="1411">SIGN UP</text>
      <text class="footer-copy" x="157" y="1423">© Copyright 2020 Mirvo . All Rights Reserved</text>
      <rect x="314" y="1394" width="16" height="16" fill="#ffffff"/>
      <text class="partner-name" x="322" y="1431" text-anchor="middle">helpdock</text>
    </g>
  </defs>

  <rect width="2231" height="1652" fill="var(--board)"/>

  <g transform="translate(67,105)" filter="url(#page-shadow)">
    <rect width="398" height="1442" fill="#ffffff"/>
    <rect width="398" height="250" fill="url(#hero-1)" role="img" aria-label="Photo of a smiling woman in glasses working at a computer"/>
    <use href="#page-body"/>
  </g>
  <g transform="translate(492,105)" filter="url(#page-shadow)">
    <rect width="398" height="1442" fill="#ffffff"/>
    <rect width="398" height="250" fill="url(#hero-2)" role="img" aria-label="Photo of a woman in glasses thinking at her desk"/>
    <use href="#page-body"/>
  </g>
  <g transform="translate(917,105)" filter="url(#page-shadow)">
    <rect width="398" height="1442" fill="#ffffff"/>
    <rect width="398" height="250" fill="url(#hero-3)" role="img" aria-label="Close-up photo of hands typing on a laptop"/>
    <use href="#page-body"/>
  </g>
  <g transform="translate(1342,105)" filter="url(#page-shadow)">
    <rect width="398" height="1442" fill="#ffffff"/>
    <rect width="398" height="250" fill="url(#hero-4)" role="img" aria-label="Photo of a laptop on a wooden desk beside a coffee cup"/>
    <use href="#page-body"/>
  </g>
  <g transform="translate(1767,105)" filter="url(#page-shadow)">
    <rect width="398" height="1442" fill="#ffffff"/>
    <rect width="398" height="250" fill="url(#hero-5)" role="img" aria-label="Photo of a smiling man working on a laptop in an office"/>
    <use href="#page-body"/>
  </g>
</svg>
</body>
</html>
```